Energy trading company (Voltarix) needs a business card

We need a business card for a company based in Central America. Our main purpose is trading energy . We already have the logo but we need some good creativity to design a high impact business card. Colors blue, orange, green can be used or we would like to see good combinatios with our logo

Target Market(s)

Energy

Industry/Entity Type

Power Generation

Contact Information for Business Card

Logo , headquarters , name, background

Font styles to use
Serif
Sans Serif

Colors

Designer to choose colors to be used in the design.

Requirements
Must have
• it must have a fresh and clean view
Nice to have
• good backgrounds that combine with the logo
Should not have
• too much words

```html
<!DOCTYPE html>
<html lang="en">
<head>
<meta charset="utf-8">
<title>Voltarix Business Card</title>
<link rel="stylesheet" href="https://fonts.googleapis.com/css2?family=Lato:wght@400;700&display=swap">
<style>
  :root {
    --stage: #d9d9d9;
    --paper: #fcf8f7;
    --orange: #f7941d;
    --green: #5bbb22;
    --ink: #1d1d1d;
    --rule: #e3dedd;
    --white: #ffffff;
  }
  * { box-sizing: border-box; margin: 0; padding: 0; }
  html, body {
    width: 1200px; height: 782px; overflow: hidden;
    background: var(--stage);
    font-family: "Lato", Arial, sans-serif;
  }
  .stage {
    width: 1200px; height: 782px;
    display: flex; align-items: center; justify-content: center; gap: 60px;
  }
  .card {
    position: relative;
    width: 520px; height: 300px;
    box-shadow: 0 6px 18px rgba(0,0,0,0.18);
    overflow: hidden;
  }
  /* Front */
  .card-front { background: var(--paper); }
  .brand {
    position: absolute; left: 34px; top: 118px;
    display: flex; align-items: center; gap: 12px;
  }
  .brand-mark {
    width: 22px; height: 22px; border-radius: 50%;
    background: var(--orange);
  }
  .brand-name {
    font-weight: 400; font-size: 42px; letter-spacing: 1px;
    color: var(--green); line-height: 1;
  }
  .divider {
    position: absolute; left: 272px; top: 58px;
    width: 1px; height: 150px; background: var(--rule);
  }
  .contact {
    position: absolute; left: 292px; top: 62px;
    color: var(--ink);
  }
  .person-name {
    font-weight: 700; font-size: 17px; letter-spacing: 0.5px; line-height: 1.1;
  }
  .person-name .first { color: var(--orange); }
  .person-name .last { color: var(--green); }
  .person-role { font-size: 14px; margin-bottom: 6px; }
  .contact-list { list-style: none; font-size: 14px; line-height: 1.35; }
  .contact-list li { display: flex; align-items: center; gap: 6px; }
  .contact-list svg { width: 11px; height: 11px; flex: none; }
  .address { font-size: 14px; line-height: 1.3; margin-top: 4px; }
  .bands { position: absolute; left: 0; bottom: 0; width: 520px; height: 60px; }

  /* Back */
  .card-back { background: var(--orange); }
  .back-field { position: absolute; inset: 0; background: var(--orange); }
  .back-brand {
    position: absolute; left: 300px; top: 134px;
    display: flex; align-items: center; gap: 10px;
  }
  .back-brand .brand-mark { background: var(--white); width: 18px; height: 18px; }
  .back-brand .brand-name { color: var(--white); font-size: 26px; }
</style>
</head>
<body>
<main class="stage">
  <section class="card card-front" aria-label="Business card front">
    <div class="brand">
      <span class="brand-mark"></span>
      <span class="brand-name">VOLTARIX</span>
    </div>
    <div class="divider"></div>
    <div class="contact">
      <p class="person-name"><span class="first">DANIEL</span> <span class="last">MORENO</span></p>
      <p class="person-role">Managing Director</p>
      <ul class="contact-list">
        <li>
          <svg viewBox="0 0 12 12" aria-hidden="true"><path fill="var(--orange)" d="M2.5 1 L4.5 1 L5.2 3.6 L4 4.6 Q5 6.8 7.4 8 L8.4 6.8 L11 7.5 L11 9.5 Q11 11 9.5 11 Q1 10 1 2.5 Q1 1 2.5 1 Z"/></svg>
          055-987 654 321
        </li>
        <li>
          <svg viewBox="0 0 12 12" aria-hidden="true"><rect x="0.5" y="2" width="11" height="8" fill="var(--orange)"/><path d="M0.5 2 L6 6.5 L11.5 2" fill="none" stroke="var(--paper)" stroke-width="1"/></svg>
          hello@voltarix.com
        </li>
        <li>
          <svg viewBox="0 0 12 12" aria-hidden="true"><circle cx="6" cy="6" r="5.5" fill="var(--orange)"/><path d="M0.5 6 H11.5 M6 0.5 Q3 6 6 11.5 M6 0.5 Q9 6 6 11.5" fill="none" stroke="var(--paper)" stroke-width="0.8"/></svg>
          www.voltarix.com
        </li>
      </ul>
      <p class="address">18 Solar Avenue<br>San José, 10101</p>
    </div>
    <svg class="bands" viewBox="0 0 520 60" aria-hidden="true">
      <polygon points="0,34 282,34 270,46 0,46" fill="var(--orange)"/>
      <polygon points="290,34 520,34 520,60 262,60" fill="var(--green)"/>
    </svg>
  </section>

  <section class="card card-back" aria-label="Business card back">
    <div class="back-field" role="img" aria-label="Faint repeating brand pattern on orange background"></div>
    <div class="back-brand">
      <span class="brand-mark"></span>
      <span class="brand-name">VOLTARIX</span>
    </div>
  </section>
</main>
</body>
</html>
```